We need a brochure for our project Caelum Petra

Hi!
We need a brochure for our project!
The designer can check out our website: caelum-petrix.com (to see what it's about)
The designer can choose the brochure layout and fold, as the designer sees fit. The designer can also format text as he sees fit.
We'd like the style to be minimal, but still not too blank, (if it makes sense).
Our name is Caelum Petra, meaning Sky Stone, so think in terms of green and brown, environmental.
We are attaching materials that should go on the brochure, as well as text, also the explanation of the render since some arrows should be added to point to what is going in and what goes out. What we want to present is a circular economy around the render.
I will also attach the work our previous designer did, and we would go for something different at this point (but the image inside shows circular economy and what goes out and in well, so that should somehow be transferred around the render).

Thank you,
Caelum Petra team

```html
<!DOCTYPE html>
<html lang="en">
<head>
<meta charset="utf-8">
<title>Caelum Petra Brochure</title>
<link href="https://fonts.googleapis.com/css2?family=Montserrat:wght@400;500;600;700;800;900&display=swap" rel="stylesheet">
<style>
:root{
  --green:#008a4b;
  --green-dark:#0b6b3c;
  --brown:#5a2e22;
  --ink:#2e2420;
  --paper:#f7f7f7;
  --paper-soft:#efefef;
  --stage:#e4e4e4;
  --rule:#008a4b;
}
*{margin:0;padding:0;box-sizing:border-box}
html,body{width:860px;height:1200px;overflow:hidden}
body{background:var(--stage);font-family:"Montserrat",Arial,sans-serif;color:var(--ink);position:relative}
.spread{position:absolute;left:40px;width:780px;height:552px;display:flex;box-shadow:0 6px 18px rgba(0,0,0,.18)}
.spread--outer{top:32px}
.spread--inner{top:616px;border-bottom:2px solid var(--green)}
.page{position:relative;width:390px;height:552px;background:var(--paper);overflow:hidden}
.page--front{background:var(--paper-soft)}
.abs{position:absolute}
/* back page */
.usage-title{left:42px;top:36px;font-size:12.5px;font-weight:500;color:var(--brown);letter-spacing:.2px}
.usage-title b{color:var(--green);font-weight:800}
.usage-rule{left:42px;top:57px;width:298px;height:1px;background:var(--rule)}
.usage-list{list-style:none;font-size:9px;line-height:1.25;color:var(--ink)}
.usage-list li{position:relative;padding-left:22px;margin-bottom:8px}
.usage-list li::before{content:"";position:absolute;left:0;top:0;width:11px;height:11px;border-radius:50%;border:1.5px solid var(--green)}
.usage-list li::after{content:"";position:absolute;left:4px;top:2px;width:3px;height:5px;border:solid var(--green);border-width:0 1.5px 1.5px 0;transform:rotate(40deg)}
.usage-list--a{left:42px;top:72px;width:160px}
.usage-list--b{left:206px;top:72px;width:130px}
.usage-list--b li:nth-child(2){margin-top:12px}
.usage-list--b li:nth-child(3){margin-top:12px}
.sample-photo{left:43px;top:189px;width:292px;height:183px;border:4px solid #fff;background:radial-gradient(ellipse at 50% 55%,#c9c9c6 0%,#a9a9a5 55%,#8d8d89 100%);box-shadow:0 6px 8px -4px rgba(0,0,0,.25)}
.contact-band{left:0;top:397px;width:390px;height:155px;background:var(--green)}
.contact-title{left:43px;top:423px;font-size:12.5px;color:#fff;font-weight:500;letter-spacing:.3px}
.contact-title b{font-weight:800}
.contact-rule{left:43px;top:441px;width:135px;height:1px;background:rgba(255,255,255,.7)}
.contact-lines{left:43px;top:450px;color:#fff;font-size:8.6px;line-height:1.3}
.contact-lines p{position:relative;padding-left:11px}
.contact-lines p + p{margin-top:8px}
.contact-lines svg{position:absolute;left:0;top:2px}
.name-box{left:212px;top:397px;width:121px;height:97px;background:#fff;border-radius:0 0 4px 4px;display:flex;align-items:center;justify-content:center;gap:5px}
.brand-dot{width:11px;height:11px;border-radius:50%;background:var(--green)}
.brand-name{font-weight:500;color:var(--green);letter-spacing:1px;text-transform:uppercase}
.name-box .brand-name{font-size:10.5px}
.contact-web{left:216px;top:519px;color:#fff;font-size:8.6px;display:flex;align-items:center;gap:4px}
/* front page */
.front-brand{left:0;top:44px;width:390px;display:flex;justify-content:center;align-items:center;gap:10px}
.front-brand .brand-dot{width:26px;height:26px}
.front-brand .brand-name{font-size:24px;letter-spacing:2px}
.hero-photo{left:0;top:131px;width:390px;height:266px;background:radial-gradient(circle at 72% 50%,#7fb24a 0%,#3f8a3a 26%,#2f7a44 34%,#7d3f24 36%,#a0512e 60%,#8a4123 100%)}
.front-title{left:52px;top:420px;width:286px;height:25px;background:var(--green);color:#fff;font-size:16px;font-weight:500;text-align:center;line-height:25px;letter-spacing:.6px}
.front-sub{left:40px;top:446px;width:310px;text-align:center;color:var(--brown);font-size:18.5px;font-weight:900;letter-spacing:.3px}
.front-tag{left:30px;top:472px;width:330px;text-align:center;font-size:7.4px;color:var(--ink)}
.front-hash{left:30px;top:485px;width:330px;text-align:center;font-size:8.6px;color:#1d9a5a;font-weight:700}
.front-rule{left:52px;top:507px;width:286px;height:1px;background:var(--rule)}
.front-url{left:30px;top:516px;width:330px;text-align:center;font-size:8.5px;letter-spacing:4.2px;color:var(--ink);font-weight:500}
/* inner left */
.soil-photo{left:0;top:0;width:390px;height:215px;background:linear-gradient(115deg,#3d3425 0%,#5a4a34 40%,#6e5a40 60%,#2e2719 100%)}
.bar{left:40px;width:301px;height:27px;background:var(--green);color:#fff;font-size:13.5px;font-weight:500;padding-left:20px;line-height:27px;letter-spacing:.3px;border-radius:0 0 3px 3px}
.bar b{font-weight:800}
.bar--challenge{top:202px}
.bar--invest{top:352px;border-radius:3px}
.bar--carbon{top:451px;border-radius:3px}
.sub-head{left:40px;font-size:8.6px;font-weight:600;color:var(--ink)}
.sub-head--sludge{top:235px}
.sub-head--process{top:486px}
.body-notes{left:40px;top:250px;width:300px;font-size:6.4px;line-height:1.45;color:var(--ink)}
.body-notes p{border-left:1px solid var(--brown);padding-left:6px;margin-bottom:5px;text-align:justify}
.body-notes em{font-style:normal;color:var(--green);font-weight:700}
.tick-list{list-style:none;font-size:6.5px;line-height:1.8;color:var(--ink)}
.tick-list li{position:relative;padding-left:10px}
.tick-list li::before{content:"";position:absolute;left:0;top:2.5px;width:6px;height:6px;border-radius:50%;border:1px solid var(--green)}
.invest-list{left:50px;top:387px}
.roi{left:40px;top:417px;font-size:8.8px;font-weight:700;color:var(--green)}
.process-list{left:40px;top:502px;display:flex;gap:18px;font-size:7.6px;font-weight:700;color:var(--ink)}
.process-list span{position:relative;padding-left:10px}
.process-list span::before{content:"";position:absolute;left:0;top:1.5px;width:6px;height:6px;border-radius:50%;border:1px solid var(--green)}
/* inner right */
.plant-render{left:0;top:140px;width:390px;height:262px;background:linear-gradient(160deg,#f1f1f3 0%,#e0e3ea 45%,#d0d5de 100%)}
.callouts{left:0;top:0}
.callout{font-size:10px;font-weight:700;color:var(--brown);letter-spacing:.3px;line-height:1.2}
.callout small{display:block;font-size:7.4px;font-weight:400;color:var(--ink);letter-spacing:0}
.callout--wash{left:259px;top:50px}
.callout--ash{left:259px;top:85px}
.callout--mineral{left:258px;top:120px}
.callout--end{left:258px;top:168px}
.co2-title{left:20px;top:437px;width:350px;text-align:center;font-size:13.2px;font-weight:700;line-height:1.3}
.co2-title span{display:block}
.co2-title .g{color:var(--green-dark)}
.co2-title .b{color:var(--brown)}
.co2-rule{left:52px;top:481px;width:286px;height:1px;background:var(--rule)}
.specs{left:52px;top:492px;width:290px;display:grid;grid-template-columns:145px 145px;row-gap:6px;font-size:8.6px;color:var(--ink)}
.specs span{position:relative;padding-left:12px}
.specs span::before{content:"";position:absolute;left:0;top:2px;width:6px;height:6px;border-radius:50%;border:1px solid var(--ink)}
.specs b{color:var(--green);font-weight:600}
</style>
</head>
<body>

<section class="spread spread--outer">
  <div class="page page--back">
    <h2 class="abs usage-title">USAGE OF <b>CONSTRUCTION COMPOSITE</b></h2>
    <div class="abs usage-rule"></div>
    <ul class="abs usage-list usage-list--a">
      <li>Water impermeable landfill capping.</li>
      <li>Roadbed construction.</li>
      <li>Ant flooding embankments construction.</li>
      <li>Other construction elements (blocks, bricks).</li>
    </ul>
    <ul class="abs usage-list usage-list--b">
      <li>Road and service areas on landfills construction.</li>
      <li>Sewage pipelines bed construction.</li>
      <li>Road embankments construction.</li>
    </ul>
    <div class="abs sample-photo" role="img" aria-label="Photo of a grey cylindrical composite test sample on concrete"></div>

    <div class="abs contact-band"></div>
    <h3 class="abs contact-title">CONTACT <b>INFO</b></h3>
    <div class="abs contact-rule"></div>
    <div class="abs contact-lines">
      <p><svg width="6" height="8" viewBox="0 0 6 8"><circle cx="3" cy="2.5" r="2" fill="none" stroke="#fff" stroke-width=".8"/><path d="M3 4.5V8" stroke="#fff" stroke-width=".8"/></svg>Strata Works d.o.o.<br>Brezova ulica 12,<br>4100 Novo Polje,<br>Slovenia</p>
      <p><svg width="7" height="7" viewBox="0 0 7 7"><circle cx="3.5" cy="3.5" r="3" fill="none" stroke="#fff" stroke-width=".8"/></svg>+386 00 12 3456</p>
      <p><svg width="7" height="6" viewBox="0 0 7 6"><rect x=".4" y=".4" width="6.2" height="5" fill="none" stroke="#fff" stroke-width=".8"/><path d="M.4.4 3.5 3 6.6.4" fill="none" stroke="#fff" stroke-width=".8"/></svg>info@strataworks.si</p>
    </div>
    <div class="abs name-box"><span class="brand-dot"></span><span class="brand-name">Caelum Petra</span></div>
    <div class="abs contact-web"><svg width="7" height="7" viewBox="0 0 7 7"><circle cx="3.5" cy="3.5" r="3" fill="none" stroke="#fff" stroke-width=".8"/><path d="M.5 3.5h6M3.5.5v6" stroke="#fff" stroke-width=".6"/></svg>www.caelum-petrix.com</div>
  </div>

  <div class="page page--front">
    <div class="abs front-brand"><span class="brand-dot"></span><span class="brand-name">Caelum Petra</span></div>
    <div class="abs hero-photo" role="img" aria-label="Photo of red soil with seedlings and hands holding a young plant in moss"></div>
    <h1 class="abs front-title">TECHNICAL SOLUTION FOR</h1>
    <div class="abs front-sub">MAJOR ECOLOGICAL ISSUE</div>
    <p class="abs front-tag">Caelum Petra is an inspirational movement that has decided to promote</p>
    <p class="abs front-hash">#necessary change</p>
    <div class="abs front-rule"></div>
    <p class="abs front-url">www.caelum-petrix.com</p>
  </div>
</section>

<section class="spread spread--inner">
  <div class="page page--inside-left">
    <div class="abs soil-photo" role="img" aria-label="Photo of cupped hands holding dark soil"></div>
    <h2 class="abs bar bar--challenge">GLOBAL <b>CHALLENGE:</b></h2>
    <h3 class="abs sub-head sub-head--sludge">Dealing With Waste Sludge:</h3>
    <div class="abs body-notes">
      <p>Technology line - TL directly answers the burning issue of waste sludge, and with it's patented mineralisation process turns sludge into valuable and safe composite; to be used mainly in construction.</p>
      <p><em>TECHNOLOGY LINE - TL</em> is approved by the Regional Agency for Green Innovation (RAGI);</p>
      <p><em>TL</em> is a <em>GREEN TECHNOLOGY</em> and is fully certified and recognised by the most trusted authorities.</p>
    </div>
    <h2 class="abs bar bar--invest">SUPERIOR <b>INVESTMENT:</b></h2>
    <ul class="abs tick-list invest-list">
      <li>Sludge disposal costs increase daily with no other sustainable solution in sight.</li>
      <li>Unique business opportunity with no current competition.</li>
    </ul>
    <p class="abs roi">Investor can expect a full ROI in under 2 years.</p>
    <h2 class="abs bar bar--carbon">CARBON <b>NEGATIVE TECHNOLOGY</b></h2>
    <h3 class="abs sub-head sub-head--process">Technology Line Can Process:</h3>
    <div class="abs process-list"><span>MUNICIPAL SLUDGE</span><span>INDUSTRIAL SLUDGE</span><span>WASTE ASH</span></div>
  </div>

  <div class="page page--inside-right">
    <div class="abs plant-render" role="img" aria-label="3D render of the processing line: loader, hopper, silo, conveyors and dump truck"></div>
    <svg class="abs callouts" width="390" height="300" viewBox="0 0 390 300">
      <g fill="none" stroke="#0b6b3c" stroke-width="1">
        <path d="M252 57H138V266"/>
        <path d="M252 92H198V152"/>
        <path d="M252 127H244V287"/>
        <path d="M298 203V287"/>
      </g>
      <g fill="#0b6b3c">
        <circle cx="138" cy="266" r="3"/>
        <circle cx="198" cy="152" r="3.5"/>
        <circle cx="244" cy="287" r="3"/>
        <circle cx="298" cy="287" r="3"/>
      </g>
    </svg>
    <div class="abs callout callout--wash">WASH SLUDGE</div>
    <div class="abs callout callout--ash">WASTE ASH</div>
    <div class="abs callout callout--mineral">MINERALIZATION<br>PROCESS</div>
    <div class="abs callout callout--end">END PRODUCT<small>(reusable composite<br>suitable for construction)</small></div>
    <h2 class="abs co2-title"><span class="g">CO2 TAKEN OUT OF THE ATMOSPHERE</span><span class="b">CARBON NEGATIVE TECHNOLOGY</span></h2>
    <div class="abs co2-rule"></div>
    <div class="abs specs">
      <span><b>Lifespan:</b> 20 years</span>
      <span><b>Size:</b> 15x20m2</span>
      <span><b>Capacity:</b> 21.600T/year</span>
      <span><b>Warranty:</b> 24 months</span>
    </div>
  </div>
</section>

</body>
</html>
```